Thermostat Screen Design

We need a screen layout design for a new thermostat we're currently developing. If you're not familiar with thermostats, you can see some examples here - http://smart-climate-units-guide.bestpickdigest.com/

We're after the main page design, with icons, colours etc. It needs to be clean, modern and minimalistic. Attached is all components required on the screen. The screen size is 5 inch (diagnol).

The arrows on the screen showcase what happens when you press a button. For example, when you press MODE once you get OFF, press it twice, HEAT, press it 3 times, COOL, etc. This is just for your reference.

You have complete creative license on how you choose to layout the screen, position the components etc, but we require:

- it must be on a 5 inch screen diagnol
- modern, clean and minimalistic
- includes icons and colours
- Intuitive

Let me know if any questions.

```html
<!DOCTYPE html>
<html lang="en">
<head>
<meta charset="utf-8">
<title>Thermostat Main Screen</title>
<link rel="stylesheet" href="https://fonts.googleapis.com/css2?family=Iceland&display=block">
<style>
  :root {
    --bg: #000000;
    --stripe: #1c1c1c;
    --orange: #ff8a00;
    --orange-soft: #ff9a2a;
    --blue: #0a64ff;
    --blue-light: #4b8dff;
    --blue-text: #5b8ff5;
    --white: #ffffff;
  }
  * { margin: 0; padding: 0; box-sizing: border-box; }
  html, body { width: 1200px; height: 960px; overflow: hidden; background: var(--bg); }
  .screen {
    position: relative;
    width: 1200px; height: 960px; overflow: hidden;
    background-color: var(--bg);
    background-image: repeating-linear-gradient(90deg, var(--stripe) 0 1px, transparent 1px 7px);
    font-family: "Iceland", "Arial Narrow", "Roboto Condensed", sans-serif;
    font-weight: 400;
    text-transform: uppercase;
    white-space: nowrap;
    line-height: 1;
  }
  .abs { position: absolute; }
  .date {
    left: 246px; top: 40px;
    font-size: 50px; letter-spacing: 4px; word-spacing: 12px;
    color: var(--blue-text);
  }
  .pill {
    display: flex; align-items: center; justify-content: center;
    border-radius: 9px; color: var(--white);
    white-space: nowrap; overflow: hidden;
  }
  .pill--orange { background: var(--orange); }
  .pill--blue { background: var(--blue); }
  .pill--light { background: var(--blue-light); }
  .top-btn { top: 21px; width: 124px; height: 45px; font-size: 26px; letter-spacing: 1px; }
  .sleep { left: 836px; }
  .zone-current { left: 990px; }
  .clock { left: 864px; top: 110px; }

  .side-btn { left: 43px; width: 90px; height: 90px; font-size: 20px; border-radius: 8px; }
  .side-btn.mode { top: 250px; }
  .side-btn.fan { top: 369px; }
  .side-btn.settings { top: 488px; font-size: 17px; }
  .side-btn.zones { top: 606px; font-size: 17px; }

  .reading-label { top: 252px; font-size: 23px; color: var(--orange); letter-spacing: 1px; }
  .outdoor-label { left: 298px; }
  .humidity-label { left: 483px; }
  .outdoor-arc { left: 290px; top: 284px; }
  .reading-value { top: 300px; font-size: 46px; color: var(--orange); letter-spacing: 2px; }
  .outdoor-value { left: 350px; }
  .outdoor-dot { left: 396px; top: 297px; width: 6px; height: 6px; border-radius: 50%; background: var(--orange); }
  .humidity-value { left: 497px; }

  .dial { left: 291px; top: 383px; }
  .room-value {
    left: 396px; top: 495px; width: 100px;
    font-size: 96px; color: var(--blue); letter-spacing: 2px;
  }
  .room-dot { left: 489px; top: 494px; width: 12px; height: 12px; border-radius: 50%; background: var(--blue); }
  .room-label {
    left: 342px; top: 622px; width: 202px; height: 56px;
    background: var(--orange); color: var(--white);
    font-size: 42px; letter-spacing: 2px;
    display: flex; align-items: center; justify-content: center;
    white-space: nowrap; overflow: hidden;
  }

  .setpoint-label {
    left: 600px; width: 242px; text-align: right;
    font-size: 30px; letter-spacing: 2px; color: var(--blue-text);
  }
  .heat-label { top: 460px; }
  .cool-label { top: 560px; }
  .setpoint-btn { left: 858px; }
  .heat-btn { top: 443px; }
  .cool-btn { top: 545px; }

  .option-bar { top: 849px; height: 42px; font-size: 19px; letter-spacing: 0.5px; word-spacing: 3px; }
  .opt-mode { left: 70px; width: 251px; }
  .opt-fan { left: 346px; width: 191px; }
  .opt-mode-icons { left: 561px; width: 225px; }
  .opt-zones { left: 811px; width: 291px; }
</style>
</head>
<body>
<main class="screen">
  <div class="abs date">Wed July 2014</div>

  <div class="abs pill pill--orange top-btn sleep">Sleep</div>
  <div class="abs pill pill--blue top-btn zone-current">Zone 1</div>

  <svg class="abs clock" width="226" height="226" viewBox="0 0 226 226" aria-label="Analog clock">
    <circle cx="113" cy="113" r="109" fill="none" stroke="var(--orange-soft)" stroke-width="2.5"/>
    <g stroke="var(--orange-soft)" stroke-width="4">
      <line x1="113" y1="17" x2="113" y2="29"/>
      <line x1="113" y1="197" x2="113" y2="209"/>
      <line x1="17" y1="113" x2="29" y2="113"/>
      <line x1="197" y1="113" x2="209" y2="113"/>
      <line x1="161" y1="30" x2="156" y2="39"/>
      <line x1="196" y1="65" x2="187" y2="70"/>
      <line x1="196" y1="161" x2="187" y2="156"/>
      <line x1="161" y1="196" x2="156" y2="187"/>
      <line x1="65" y1="196" x2="70" y2="187"/>
      <line x1="30" y1="161" x2="39" y2="156"/>
      <line x1="30" y1="65" x2="39" y2="70"/>
      <line x1="65" y1="30" x2="70" y2="39"/>
    </g>
    <line x1="113" y1="113" x2="113" y2="48" stroke="var(--orange-soft)" stroke-width="4"/>
    <line x1="113" y1="113" x2="179" y2="151" stroke="var(--orange-soft)" stroke-width="3"/>
    <line x1="113" y1="113" x2="87" y2="97" stroke="var(--orange-soft)" stroke-width="3"/>
    <circle cx="113" cy="113" r="4" fill="var(--orange-soft)"/>
  </svg>

  <nav>
    <div class="abs pill pill--orange side-btn mode">Mode</div>
    <div class="abs pill pill--blue side-btn fan">Fan</div>
    <div class="abs pill pill--orange side-btn settings">Settings</div>
    <div class="abs pill pill--blue side-btn zones">Zones</div>
  </nav>

  <div class="abs reading-label outdoor-label">Outdoor Tem</div>
  <div class="abs reading-label humidity-label">Indoor RH</div>
  <svg class="abs outdoor-arc" width="60" height="78" viewBox="0 0 60 78" aria-hidden="true">
    <defs>
      <linearGradient id="arcFade" x1="0" y1="0" x2="1" y2="0">
        <stop offset="0.3" stop-color="var(--orange)"/>
        <stop offset="1" stop-color="var(--orange)" stop-opacity="0"/>
      </linearGradient>
    </defs>
    <path d="M50 6 A34 34 0 0 0 50 72" fill="none" stroke="url(#arcFade)" stroke-width="10"/>
  </svg>
  <div class="abs reading-value outdoor-value">30</div>
  <div class="abs outdoor-dot"></div>
  <div class="abs reading-value humidity-value">45%</div>

  <svg class="abs dial" width="314" height="314" viewBox="0 0 314 314" aria-hidden="true">
    <defs>
      <linearGradient id="dialFade" x1="0" y1="0" x2="0" y2="1">
        <stop offset="0" stop-color="var(--blue)"/>
        <stop offset="0.45" stop-color="var(--blue-light)"/>
        <stop offset="0.72" stop-color="var(--blue)"/>
        <stop offset="0.88" stop-color="var(--blue)" stop-opacity="0"/>
      </linearGradient>
    </defs>
    <circle cx="157" cy="157" r="134" fill="none" stroke="url(#dialFade)" stroke-width="39"/>
  </svg>
  <div class="abs room-value">30</div>
  <div class="abs room-dot"></div>
  <div class="abs room-label">Room Tem</div>

  <div class="abs setpoint-label heat-label">Heat Set Point</div>
  <div class="abs setpoint-label cool-label">Cool Set Point</div>
  <svg class="abs setpoint-btn heat-btn" width="60" height="60" viewBox="0 0 60 60" aria-label="Raise set point">
    <circle cx="30" cy="30" r="28" fill="none" stroke="var(--blue-light)" stroke-width="2.5"/>
    <path d="M30 12 L48 38 L30 31 L12 38 Z" fill="var(--blue-light)"/>
  </svg>
  <svg class="abs setpoint-btn cool-btn" width="60" height="60" viewBox="0 0 60 60" aria-label="Lower set point">
    <circle cx="30" cy="30" r="28" fill="none" stroke="var(--blue-light)" stroke-width="2.5"/>
    <path d="M30 48 L48 22 L30 29 L12 22 Z" fill="var(--blue-light)"/>
  </svg>

  <footer>
    <div class="abs pill pill--orange option-bar opt-mode">Off Heat&nbsp; Cool Auto</div>
    <div class="abs pill pill--orange option-bar opt-fan">Fan Icons: Auto</div>
    <div class="abs pill pill--light option-bar opt-mode-icons">Mode Icons: Heat Cool</div>
    <div class="abs pill pill--light option-bar opt-zones">Zone 1&nbsp; Zone 2&nbsp; Zone 3&nbsp; Zone 4</div>
  </footer>
</main>
</body>
</html>
```